House Builder and Property Development Card Design and Logo

I need a business card design for a building and property development company.
Colour scheme of Dark Grey and Green, I would like it bold, sharp and professional.
No logo yet done, I'm open to options but please stay away from the usual- house, roof, hammers etc.
Thanks Rob

Please be aware that on the business card information section the WHRC # 5528391 is a licence number and my phone number 0492837165. The numbers are close together and could be mistaken as one whole number 

Thank you

                                   

Industry/Entity Type

Building

Contact Information for Business Card

VARGA BUILD & DEVELOPMENT.
Residential Building & Property Development
Robert Varga - Director
WHRC # 5528391
0492837165
rob@vargabuild.example.com.au

Requirements
Must have
• Bold Business name
Dark grey and green colours
Should not have
• roof outline or hammer logo

```html
<!DOCTYPE html>
<html lang="en">
<head>
<meta charset="utf-8">
<title>Varga Build &amp; Development – Business Card</title>
<link rel="stylesheet" href="https://fonts.googleapis.com/css2?family=Saira:wght@500&family=Noto+Sans:wght@400;600;700&display=swap">
<style>
  :root {
    --bg: #a6dca8;
    --card-dark-top: #232323;
    --card-dark-body: #141414;
    --card-light: #ffffff;
    --green: #00894a;
    --ink: #1c1c1c;
    --muted: #7a7a7a;
    --white: #ffffff;
  }
  html, body {
    margin: 0;
    width: 800px;
    height: 1200px;
    overflow: hidden;
    background: var(--bg);
    font-family: "Noto Sans", sans-serif;
  }
  .canvas {
    position: relative;
    width: 800px;
    height: 1200px;
  }
  .card {
    position: absolute;
    top: 350px;
    width: 310px;
    height: 500px;
    box-shadow: 0 2px 6px rgba(0,0,0,0.25);
    overflow: hidden;
  }
  .card--front { left: 72px; background: var(--card-dark-body); }
  .card--back  { left: 419px; background: var(--card-light); }

  .wordmark {
    text-align: center;
    font-family: "Saira", sans-serif;
    font-weight: 500;
    line-height: 1;
  }
  .wordmark__name { display: block; font-size: 46px; letter-spacing: 1px; }
  .wordmark__sub  { display: block; font-size: 14px; letter-spacing: 0.8px; margin-top: 8px; }

  .front__header {
    height: 150px;
    background: var(--card-dark-top);
    box-sizing: border-box;
    padding-top: 42px;
    color: var(--white);
  }
  .front__art {
    position: absolute;
    left: 120px;
    top: 220px;
    width: 72px;
    height: 258px;
  }
  .front__band, .back__band {
    position: absolute;
    left: 0;
    bottom: 0;
    width: 100%;
    background: var(--green);
  }
  .front__band { height: 22px; }
  .back__band  { height: 16px; }

  .back__person {
    position: absolute;
    left: 45px;
    right: 0;
    top: 42px;
    border-bottom: 3px solid var(--green);
    padding-bottom: 4px;
  }
  .back__name {
    font-family: "Noto Sans", sans-serif;
    font-weight: 600;
    font-size: 21px;
    color: var(--ink);
    margin: 0;
    line-height: 1.1;
  }
  .back__role {
    font-size: 14px;
    color: var(--ink);
    margin: 0;
    letter-spacing: 0.3px;
  }
  .back__logo {
    position: absolute;
    left: 0;
    top: 142px;
    width: 100%;
    height: 83px;
    background: var(--green);
    color: var(--white);
    box-sizing: border-box;
    padding-top: 14px;
  }
  .back__logo .wordmark__name { font-size: 42px; }
  .back__logo .wordmark__sub { margin-top: 5px; }
  .back__licence {
    position: absolute;
    top: 237px;
    width: 100%;
    text-align: center;
    font-size: 12px;
    color: var(--muted);
    margin: 0;
  }
  .back__info {
    position: absolute;
    left: 45px;
    margin: 0;
    padding-left: 7px;
    border-left: 3px solid var(--green);
    color: var(--ink);
    line-height: 1.35;
  }
  .back__services { top: 346px; font-weight: 700; font-size: 15px; }
  .back__contact  { top: 408px; font-size: 15px; }
</style>
</head>
<body>
<div class="canvas">

  <section class="card card--front">
    <header class="front__header">
      <div class="wordmark">
        <span class="wordmark__name">VARGA</span>
        <span class="wordmark__sub">BUILD &amp; DEVELOPMENT</span>
      </div>
    </header>
    <svg class="front__art" role="img" aria-label="Dark silhouette illustration of a tall skyscraper with diagonal bracing" viewBox="0 0 72 258">
      <defs>
        <linearGradient id="tower-tone" x1="0" y1="0" x2="0" y2="1">
          <stop offset="0" stop-color="#161616"/>
          <stop offset="1" stop-color="#0c0c0c"/>
        </linearGradient>
      </defs>
      <rect width="72" height="258" fill="url(#tower-tone)"/>
    </svg>
    <div class="front__band"></div>
  </section>

  <section class="card card--back">
    <div class="back__person">
      <p class="back__name">ROBERT VARGA</p>
      <p class="back__role">DIRECTOR</p>
    </div>
    <div class="back__logo wordmark">
      <span class="wordmark__name">VARGA</span>
      <span class="wordmark__sub">BUILD &amp; DEVELOPMENT</span>
    </div>
    <p class="back__licence">WHRC # 5528391</p>
    <p class="back__info back__services">Residential Building &amp;<br>Property Development</p>
    <p class="back__info back__contact">04 9283 7165<br>rob@vargabuild.example.com.au</p>
    <div class="back__band"></div>
  </section>

</div>
</body>
</html>
```